Forex website redesign

We need an attractive good looking website design that increase the apatite of our visitors to subscribe to our advisory service, beside the fact that we do offer very high quality service.

Our service is where we connect to investor accounts who are subscribed, to automatically deliver and execute our advise to buy or sell straight onto their account using high tech software.

The final design should communicate financial safty and growth.
Updates

Here is something to keep in mind about our business model that may help you in your design, we SHOW people the right way to invest, so they can make money instead of going somewere else and lose it. Beside that point, most websites in forex that includes pictures of happy and excited people who make money ALWAY turn out to be scam. So please try not to position our business that way in visitor first impression once he/she visit our site.

Thank you for your help :)

Target Market(s)

Financial Market, 20-70 years old

Industry/Entity Type

Financial

Requirements
Must have
• Call to action feature + Logo redesign. Please visit www.brelvantrade.net to get an idea of how we want it. Also include the personal photos of our advisors in your deign.

```html
<!DOCTYPE html>
<html lang="en">
<head>
<meta charset="utf-8">
<title>Brelvan Trade Ltd.</title>
<link href="https://fonts.googleapis.com/css2?family=Mulish:ital,wght@0,300;0,400;0,600;0,700;0,800;1,700;1,800&family=Open+Sans:wght@400;600;700&display=swap" rel="stylesheet">
<style>
:root{
  --blue:#0d5aa7;
  --blue-dark:#0a3f7e;
  --blue-deep:#083a78;
  --sky:#3a9ad9;
  --green:#2f9f1f;
  --lime:#8cc21a;
  --pale:#e4edf6;
  --grey:#ececec;
  --text:#333;
  --orange:#f7a21b;
}
*{margin:0;padding:0;box-sizing:border-box}
html,body{width:800px;height:1200px;overflow:hidden;background:#fff}
.page{position:absolute;left:0;top:0;width:1000px;height:1500px;transform:scale(.8);transform-origin:0 0;font-family:"Open Sans",Arial,sans-serif;color:var(--text)}
.abs{position:absolute}
/* header */
.header{left:0;top:0;width:1000px;height:87px;background:linear-gradient(#fff,#f1f1f1)}
.brand{left:95px;top:26px}
.brand-name{font-family:"Mulish",sans-serif;font-weight:800;font-size:29px;color:var(--blue);letter-spacing:-.5px;line-height:32px}
.brand-tag{font-size:12.5px;color:#222;font-style:italic;margin-top:-2px}
.utility{left:395px;top:45px;font-size:10.5px;color:#555}
.lang{left:483px;top:43px;width:88px;height:19px;border:1px solid #ccc;background:#fff;font-size:10px;padding:3px 6px;color:#333}
.lang::after{content:"";position:absolute;right:6px;top:7px;border:4px solid transparent;border-top-color:#999}
.clock{left:645px;top:16px;font-size:10.5px;color:#999}
.clock b{color:var(--sky)}
.field{top:42px;height:20px;width:105px;border:1px solid #ccc;background:#fff;font-size:9.5px;color:#aaa;padding:3px 5px}
.login{left:864px;top:42px;width:43px;height:20px;border:1px solid #bbb;border-radius:3px;background:linear-gradient(#fff,#e8e8e8);font-size:11px;color:var(--sky);text-align:center;line-height:18px;font-weight:600}
.tiny{font-size:9.5px;top:66px}
/* nav */
.nav{left:0;top:87px;width:1000px;height:40px;background:linear-gradient(var(--blue),#0c4f96);border-bottom:2px solid #0a417c}
.nav ul{list-style:none;position:absolute;left:92px;top:10px;display:flex;gap:26px}
.nav li{color:#fff;font-weight:600;font-size:14px}
.open-acc{left:766px;top:93px;width:125px;height:26px;background:linear-gradient(#3db92a,#238f17);color:#fff;font-size:12px;text-align:center;line-height:26px}
/* hero */
.hero{left:0;top:127px;width:1000px;height:308px;background:linear-gradient(var(--blue),var(--sky))}
.hero-card{left:90px;top:140px;width:819px;height:281px;background:linear-gradient(#fff,#dfe9f3);border-radius:3px;overflow:hidden}
.hero-photo{left:0;top:0;width:425px;height:281px;background:linear-gradient(135deg,#4a4d55,#8c8a82 60%,#c9c5bb)}
.hero-text{left:458px;top:176px;width:440px;font-family:"Mulish",sans-serif;font-size:24.5px;line-height:29px;color:#111;letter-spacing:-.6px}
.btn-live{left:712px;top:307px;width:166px;height:37px;background:linear-gradient(#37b028,#248f17);color:#fff;font-family:"Mulish",sans-serif;font-weight:700;font-size:18px;text-align:center;line-height:37px}
/* intro */
.intro{left:0;top:435px;width:1000px;height:128px;background:var(--grey);text-align:center;padding-top:27px;font-family:"Mulish",sans-serif;font-weight:300;font-size:20.5px;line-height:23.5px;color:#333}
.intro b{color:var(--blue);font-weight:400}
/* features */
.invest{left:99px;top:583px;width:284px;height:132px;background:var(--pale);border:1px solid #cfdbe8}
.invest h3{position:absolute;left:11px;top:14px;font-family:"Mulish",sans-serif;font-weight:600;font-size:16px;line-height:20px;color:var(--blue);letter-spacing:-.4px}
.amount{position:absolute;left:9px;top:61px;width:168px;height:29px;background:#fff;border:1px solid #d5dde6;font-size:11px;color:#aaa;padding:6px 6px}
.amount b{color:var(--blue);font-size:15px;font-weight:700}
.get{position:absolute;left:12px;top:102px;font-family:"Mulish",sans-serif;font-size:12.5px;color:var(--green);letter-spacing:-.3px}
.get::before{content:"";display:inline-block;width:10px;height:10px;border:2px solid var(--green);border-radius:50%;margin-right:6px;vertical-align:-2px}
.monitor{position:absolute;left:186px;top:22px;width:80px;height:78px}
.returns{left:395px;top:585px;width:272px;height:127px;border:1px solid #ccc}
.returns h3{position:absolute;left:9px;top:7px;font-family:"Mulish",sans-serif;font-weight:800;font-style:italic;font-size:22px;line-height:25px;color:#fff;letter-spacing:-.8px}
.brokers{left:684px;top:596px;width:220px;font-family:Arial,sans-serif;font-size:13px;line-height:17.5px;color:#111}
.brokers b{color:var(--blue);display:block}
/* signals */
.signals{left:107px;top:738px;width:265px}
.signals h2{font-family:"Mulish",sans-serif;font-weight:300;font-size:22px;color:#333;margin-bottom:6px}
.signals h2 em{font-style:italic;font-weight:800;color:var(--blue)}
.signals p{font-size:12px;line-height:16.8px;color:#333;margin-bottom:16px}
.signals a{font-size:12px;color:var(--green);font-style:italic;text-decoration:none}
.chart-panel{left:384px;top:730px;width:522px;height:267px;border:1px solid #ddd;border-radius:3px;background:#fff}
.chart-title{left:404px;top:743px;font-family:"Mulish",sans-serif;font-size:15px;color:var(--blue)}
.legend{top:741px;height:26px;border:1px solid #ddd;font-size:10px;color:#333;text-align:center;padding-top:8px}
.legend::before{content:"";position:absolute;left:25%;right:25%;top:2px;height:3px;background:var(--c)}
/* ticker */
.ticker{left:94px;top:1021px;width:814px;height:36px;border:1px solid #c8d6e4;border-radius:3px;background:linear-gradient(#fff,#e9eff5);display:flex;font-size:10px}
.ticker .label{width:154px;font-weight:600;font-size:11px;color:#111;padding:11px 0 0 9px}
.ticker .label span{color:var(--green)}
.ticker .cell{flex:1;border-left:1px solid #d5dee8;text-align:center;padding-top:4px;line-height:14px;color:#111}
.up{color:var(--green);font-size:9px}.down{color:#d01b1b;font-size:9px}
/* cta */
.cta{left:90px;top:1080px;width:819px;height:95px;background:linear-gradient(var(--blue),var(--blue-deep))}
.cta p{position:absolute;left:38px;top:29px;font-family:"Mulish",sans-serif;font-weight:300;font-size:28px;color:#fff;letter-spacing:-.3px}
.order{left:695px;top:1103px;width:166px;height:51px;border-radius:3px;background:linear-gradient(#fbb83a,#f08a0f);font-family:"Mulish",sans-serif;font-weight:800;font-size:22px;color:#3a2106;text-align:center;line-height:51px}
/* disclaimer */
.disclaimer{left:0;top:1196px;width:1000px;height:242px;background:var(--grey);padding:20px 100px 0;font-family:Arial,sans-serif;font-size:10.4px;line-height:13px;color:#333}
.disclaimer p{margin-bottom:12px}
.footer{left:0;top:1438px;width:1000px;height:62px;background:linear-gradient(var(--blue),var(--blue-dark));color:#fff;text-align:center;font-size:13px;padding-top:17px;line-height:16px}
.footer span{margin:0 6px}
</style>
</head>
<body>
<div class="page">
  <header class="header abs">
    <div class="brand abs">
      <div class="brand-name">Brelvan Trade Ltd.</div>
      <div class="brand-tag">From Traders to Traders, THE REAL DEAL</div>
    </div>
    <div class="utility abs">About &nbsp;|&nbsp; Support</div>
    <div class="lang abs">English</div>
    <div class="clock abs"><b>18 : 32</b> &nbsp;| &nbsp; 25 SEPTEMBER 2013</div>
    <div class="field abs" style="left:645px">User Name</div>
    <div class="field abs" style="left:755px">Password</div>
    <div class="login abs">Login</div>
    <div class="tiny abs" style="left:647px;color:var(--sky)">Sign up</div>
    <div class="tiny abs" style="left:758px;color:#888">forgot password?</div>
  </header>

  <nav class="nav abs">
    <ul><li>Home</li><li>About Us</li><li>Order</li><li>Performance »</li><li>Liu Maren Special</li><li>Why Us?</li><li>Contact Us</li></ul>
  </nav>
  <div class="open-acc abs">OPEN AN ACCOUNT</div>

  <section class="hero abs"></section>
  <div class="hero-card abs">
    <div class="hero-photo abs" role="img" aria-label="Portrait of the lead trader beside a desktop monitor showing a price chart"></div>
    <svg class="abs" style="left:425px;top:180px" width="394" height="101" viewBox="0 0 394 101"><path d="M0 101 L0 60 L40 40 L70 70 L110 20 L150 55 L190 30 L230 60 L270 45 L310 10 L350 45 L394 25 L394 101Z" fill="#c9dbef"/></svg>
  </div>
  <div class="hero-text abs">Mr. Daren Holt is the head of our Elite Group Traders and has A5 years of solid real live trading performance to show-off with Mr. Holt is an CTRA EXEMPT CTA...</div>
  <div class="btn-live abs">Live Results</div>

  <section class="intro abs"><b>Brelvan Trade LTD</b> is the ONLY forex signal service on this planet that provides full<br>info about the traders involved including REAL personal photos, REAL personal details<br>and portfolios, as well as YEARS of verified and consistent live trading performance.</section>

  <div class="invest abs">
    <h3>How much do you<br>have to invest?</h3>
    <div class="amount"><b>$</b> Enter an amount...</div>
    <div class="get">GET STARTED</div>
    <svg class="monitor" viewBox="0 0 80 78"><path d="M8 4 L74 10 L72 60 L6 56Z" fill="#2d3c4a"/><path d="M12 9 L69 14 L67 54 L11 50Z" fill="#1a5f8c"/><polyline points="14,40 24,30 32,36 42,20 52,34 60,24 66,30" fill="none" stroke="#bfe6ff" stroke-width="2"/><path d="M30 58 L46 60 L50 70 L26 68Z" fill="#7a8894"/><ellipse cx="38" cy="72" rx="22" ry="4" fill="#b7c3cf"/></svg>
  </div>

  <div class="returns abs">
    <svg class="abs" style="left:0;top:0" width="270" height="125" viewBox="395 585 270 125">
      <defs><linearGradient id="gr" x1="0" y1="0" x2="0" y2="1"><stop offset="0" stop-color="#8cc21a"/><stop offset="1" stop-color="#5ca218"/></linearGradient></defs>
      <rect x="395" y="585" width="270" height="125" fill="url(#gr)"/>
      <path d="M400 690 L474 662 L493 670 L537 654 L567 657 L618 636 L641 636 L661 616 L665 616 L665 710 L395 710 L395 692Z" fill="#eef5fb"/>
      <polyline points="400,690 474,662 493,670 537,654 567,657 618,636 641,636 661,616" fill="none" stroke="#8cc21a" stroke-width="2"/>
      <g fill="#fff" stroke="#8cc21a" stroke-width="2"><circle cx="400" cy="690" r="3"/><circle cx="474" cy="662" r="3"/><circle cx="493" cy="670" r="3"/><circle cx="537" cy="654" r="3"/><circle cx="567" cy="657" r="3"/><circle cx="618" cy="636" r="3"/><circle cx="641" cy="636" r="3"/><circle cx="661" cy="616" r="3"/></g>
    </svg>
    <h3>100% Annual return<br>on the investments</h3>
  </div>

  <div class="brokers abs"><b>Brokers option:</b>You can choose any broker you like, the copying software will work on your existing broker and existing accounts. The copier can support nearly every broker out there.</div>

  <div class="signals abs">
    <h2>How <em>Signals Work</em></h2>
    <p>Once you subscribe, you will be re-directed to a secure page to download and set-up the EA copier on your VPS with all the instructions you need (We provide full support, and we can set it up for you for no additional charge. Once set-up, the software is of superior quality and copies flawlessly, and you have direct and total control over your account.</p>
    <p>Whereas your subscription will be renewed automatically by the end of the cycle you choose (Monthly/OR/4 months).</p>
    <a>Read More...</a>
  </div>

  <div class="chart-panel abs"></div>
  <svg class="abs" style="left:384px;top:730px" width="522" height="267" viewBox="384 730 522 267" font-family="Open Sans, sans-serif">
    <path d="M450 879 L512 888 L573 873 L638 821 L701 866 L764 798 L826 810 L889 813 L889 966 L450 966Z" fill="#e3eef8"/>
    <g font-size="9" fill="#333" text-anchor="end"><text x="440" y="800">40,000</text><text x="440" y="824">30,000</text><text x="440" y="848">25,000</text><text x="440" y="873">20,000</text><text x="440" y="897">15,000</text><text x="440" y="921">10,000</text><text x="440" y="946">5,000</text></g>
    <g font-size="11.5" fill="#222" text-anchor="middle"><text x="512" y="985">2007</text><text x="573" y="985">2008</text><text x="636" y="985">2009</text><text x="701" y="985">2010</text><text x="763" y="985">2011</text><text x="827" y="985">2012</text></g>
    <polyline points="450,934 512,942 573,944 638,918 701,921 764,900 826,864 889,868" fill="none" stroke="#ef8b9c" stroke-width="2.5"/>
    <polyline points="450,917 512,927 573,911 638,891 701,906 764,866 826,848 889,852" fill="none" stroke="#88c8f4" stroke-width="2.5"/>
    <polyline points="450,879 512,888 573,873 638,821 701,866 764,798 826,810 889,813" fill="none" stroke="#8cbf1a" stroke-width="2.5"/>
    <g fill="#fff" stroke-width="2"><g stroke="#ef8b9c"><circle cx="512" cy="942" r="3"/><circle cx="573" cy="944" r="3"/><circle cx="638" cy="918" r="3"/><circle cx="701" cy="921" r="3"/><circle cx="764" cy="900" r="3"/><circle cx="826" cy="864" r="3"/></g><g stroke="#88c8f4"><circle cx="512" cy="927" r="3"/><circle cx="573" cy="911" r="3"/><circle cx="638" cy="891" r="3"/><circle cx="701" cy="906" r="3"/><circle cx="764" cy="866" r="3"/><circle cx="826" cy="848" r="3"/></g><g stroke="#8cbf1a"><circle cx="512" cy="888" r="3"/><circle cx="573" cy="873" r="3"/><circle cx="638" cy="821" r="3"/><circle cx="701" cy="866" r="3"/><circle cx="764" cy="798" r="3"/><circle cx="826" cy="810" r="3"/></g></g>
  </svg>
  <div class="chart-title abs">3 Years Investment In Our Portfolio</div>
  <div class="legend abs" style="left:645px;width:86px;--c:#8cbf1a">Brelvan Trade</div>
  <div class="legend abs" style="left:737px;width:73px;--c:#88c8f4">Company1</div>
  <div class="legend abs" style="left:815px;width:73px;--c:#ef8b9c">Company2</div>

  <div class="ticker abs">
    <div class="label">Brelvan Trade Option <span>Live</span></div>
    <div class="cell">KRVX / LMTO<br><span class="up">221.11</span> <span class="down">-221.3</span></div>
    <div class="cell">ZEPH / NORQ<br><span class="up">221.11</span> <span class="down">-221.3</span></div>
    <div class="cell">KRVX / LMTO<br><span class="up">221.11</span> <span class="down">-221.3</span></div>
    <div class="cell">DALV / PRIX<br><span class="up">221.11</span> <span class="down">-221.3</span></div>
    <div class="cell">KRVX / LMTO<br><span class="up">221.11</span> <span class="down">-221.3</span></div>
    <div class="cell">KRVX / LMTO<br><span class="up">221.11</span> <span class="down">-221.3</span></div>
  </div>

  <section class="cta abs"><p>Let us do the&nbsp; picks, while you enjoy the ride!</p></section>
  <div class="order abs">Order Now!</div>

  <section class="disclaimer abs">
    <p>Risk Disclaimer : All results on this web site must be regarded as hypothetical. hypothetical performance results have many inherent limitations, some of which are described below.</p>
    <p>no representation is being made that any account will or is likely to achieve profits or losses similar to those shown. in fact, there are frequently sharp differences between hypothetical performance results and the actual results subsequently achieved by any particular trading program. one of the limitations of hypothetical performance results is that they are generally prepared with the benefit of hindsight. in addition, hypothetical trading does not involve financial risk, and no hypothetical trading record can completely account for the impact of financial risk in actual trading. for example, the ability to withstand losses or to adhere to a particular trading program in spite of trading losses are material points which can also adversely affect actual trading results. there are numerous other factors related to the markets in general or to the implementation of any specific trading program which cannot be fully accounted for in the preparation of hypothetical performance results and all of which can adversely affect actual trading results. past results are not necessarily indicative of future results.</p>
    <p>Trading foreign exchange on margin carries a high level of risk, and may not be suitable for all investors. the high degree of leverage can either work against you or on your behalf. before deciding to invest in foreign exchange you should carefully consider your investment objectives, level of experience, and risk appetite. the possibility exists that you could sustain a loss of some or all of your initial investment and therefore you should not invest money that you cannot afford to lose. you should be aware of all the risks associated with foreign exchange trading, and seek advice from an independent financial advisor if you have any doubts.</p>
  </section>

  <footer class="footer abs">
    <span>Home</span><span>About Us</span><span>Order</span><span>Performance</span><span>Liu Maren Special</span><span>Terms &amp; Conditions</span><span>Why Us?</span><span>Contact Us</span><br>Copyright 2013, BrelvanTrade LTD
  </footer>
</div>
</body>
</html>
```